Investment firm needs website redesign

we want to change our site with a trendy new design. We are an investment trading firm dealing in currencies etc for retail clients. We are looking for new ideas for our website design which shows class and international reach. We want the inner pages also to be designed especially the look. We do not want the typical designs used by most sites and are looking for something new and interesting. you can review our current site www.vorquilatrade.example.

Target Market(s)

international

Industry/Entity Type

Forex

Coding

Coded - Design and coding required

Number of Pages Required

5+ page

Font styles to use
Sans Serif

Colors

Designer to choose colors to be used in the design.

Requirements
Must have
• responsive, easy to load
Nice to have
• something trendy yet sophisticated. technology is an important part of our business
Should not have
• do not want the typical designs used by most websites

```html
<!DOCTYPE html>
<html lang="en">
<head>
<meta charset="utf-8">
<title>Vorquila Trade – Home</title>
<link href="https://fonts.googleapis.com/css2?family=Lato:wght@300;400;700&display=swap" rel="stylesheet">
<style>
:root{
  --yellow:#f2be2c;
  --yellow-deep:#e6ad17;
  --slate:#3f5667;
  --slate-dark:#2f4352;
  --ink:#3a3f45;
  --muted:#8a929a;
  --line:#e3e6ea;
  --paper:#ffffff;
  --mist:#f4f6f8;
}
*{box-sizing:border-box;margin:0;padding:0}
html,body{width:1200px;height:3240px;overflow:hidden}
body{font-family:'Lato',Arial,sans-serif;color:var(--ink);background:var(--paper);position:relative}
.btn{display:inline-block;font-size:12px;font-weight:700;letter-spacing:.5px;padding:9px 22px;border-radius:18px;text-transform:uppercase}
.btn-yellow{background:var(--yellow);color:#fff}
.btn-outline{border:1px solid currentColor}

.topbar{height:22px;background:var(--slate-dark);display:flex;align-items:center;padding:0 60px;font-size:10px;color:#c9d2d9;gap:22px}
.topbar .tab{background:var(--yellow);color:#fff;height:22px;line-height:22px;padding:0 16px;font-weight:700}

.header{height:93px;display:flex;align-items:center;padding:0 60px;gap:30px;border-bottom:1px solid var(--line)}
.brand{display:flex;align-items:center;gap:10px;font-weight:700;font-size:24px;color:var(--slate);letter-spacing:1px}
.brand .dot{width:34px;height:34px;border-radius:50%;background:var(--yellow)}
.search{margin-left:60px;width:280px;height:30px;border:1px solid var(--line);border-radius:15px;font-size:11px;color:var(--muted);padding:8px 14px}
.header .btn{background:var(--slate);color:#fff}
.header .meta{margin-left:auto;text-align:right;font-size:11px;color:var(--muted);line-height:1.6}
.header .meta b{color:var(--slate);font-size:13px}
.flags{display:flex;gap:6px}
.flags i{width:16px;height:16px;border-radius:50%;background:var(--line);display:block}

.nav{height:40px;display:flex;align-items:center;justify-content:space-between;padding:0 80px;font-size:11px;font-weight:700;text-transform:uppercase;color:var(--slate);letter-spacing:.5px}

.hero{height:330px;position:relative;background:linear-gradient(180deg,#8da4b8 0%,#5d7a93 55%,#3f566a 100%);text-align:center;color:#fff;padding-top:90px}
.hero h1{font-size:34px;font-weight:300}
.hero .strap{display:inline-block;margin-top:14px;background:var(--yellow);padding:8px 26px;font-size:14px}
.hero .btn{margin-top:28px;color:#fff}

.platform{height:460px;display:flex;align-items:center;padding:0 110px;gap:40px}
.platform .copy{width:420px}
.label{color:var(--yellow);font-size:13px;font-weight:700;text-transform:uppercase;letter-spacing:1px}
.platform h2{font-size:24px;font-weight:300;color:var(--slate);margin:12px 0 14px;line-height:1.3}
.platform p{font-size:12px;line-height:1.7;color:var(--muted);margin-bottom:20px}
.devices{flex:1;height:300px;background:linear-gradient(135deg,#eef1f4,#c8d0d8);border-radius:6px}

.features{height:320px;text-align:center;padding-top:10px}
.features .intro{font-size:12px;color:var(--muted);line-height:1.6}
.feature-row{display:flex;justify-content:center;align-items:center;gap:20px;margin:36px 0 30px}
.arrow{color:var(--muted);font-size:20px}
.feature{width:200px;font-size:12px;color:var(--ink);line-height:1.5}
.feature svg{display:block;margin:0 auto 12px}
.features .btn{color:var(--slate)}

.showcase{height:575px;position:relative}
.showcase .photo{position:absolute;left:75px;top:0;width:1125px;height:280px;background:linear-gradient(120deg,#c9d2da,#8a9aa8 60%,#5f7080)}
.card{position:absolute;padding:40px 46px;color:#fff;font-size:13px;line-height:1.7}
.card h3{font-size:14px;font-weight:700;margin-bottom:14px}
.card .btn{margin-top:22px;color:#fff}
.card-yellow{left:55px;top:210px;width:585px;height:300px;background:var(--yellow)}
.card-slate{left:640px;top:190px;width:480px;height:340px;background:var(--slate)}

.why{height:505px;text-align:center;padding-top:20px}
.why h2{font-size:24px;font-weight:300;color:var(--slate);margin-top:10px}
.why-row{display:flex;justify-content:center;gap:50px;margin:50px 0 40px}
.why-item{width:180px;font-size:12px;line-height:1.6;color:var(--muted)}
.why-item b{display:block;color:var(--slate);font-size:13px}
.why-item svg{display:block;margin:0 auto 16px}
.why .btn{color:var(--slate)}

.help{height:455px;position:relative;background:var(--yellow)}
.help-deco{position:absolute;left:0;top:0;width:1200px;height:120px;background:linear-gradient(180deg,var(--paper) 0%,#fbe9b8 45%,var(--yellow) 100%)}
.help .inner{position:absolute;top:180px;left:110px;right:110px;display:flex;gap:90px;color:var(--slate)}
.help h4{font-size:16px;margin-bottom:12px}
.help .contact{font-size:12px;line-height:1.8;width:260px}
.help .contact .btn{margin-top:14px;background:var(--slate);color:#fff}
.form{display:grid;grid-template-columns:1fr 1fr;gap:12px 16px;width:620px}
.field{height:34px;background:#fff;border-radius:2px;font-size:11px;color:var(--muted);padding:10px 12px}
.form .btn{background:var(--slate);color:#fff;justify-self:start}

.footer{height:410px;background:var(--slate);color:#c9d2d9;display:flex;padding:50px 110px;gap:60px;font-size:11px;line-height:2}
.footer h5{color:#fff;font-size:11px;text-transform:uppercase;letter-spacing:.5px;margin-bottom:6px}
.footer .col{width:160px}
.store{width:120px;height:34px;background:#1f2c36;border-radius:5px;margin-bottom:8px}
.social{display:flex;gap:8px;margin-top:10px}
.social i{width:24px;height:24px;border-radius:50%;background:#56707f;display:block}
.copyright{height:30px;background:var(--slate-dark);color:#9aa8b3;font-size:10px;line-height:30px;padding:0 110px}
</style>
</head>
<body>

<div class="topbar"><span class="tab">Login</span><span>Open Account</span><span>Support</span><span>Education</span><span>Company News</span></div>

<header class="header">
  <div class="brand"><span class="dot"></span>VORQUILA</div>
  <div class="search">Search here</div>
  <span class="btn">Search</span>
  <div class="meta">Call us 24/5<br><b>+00 555 0142</b></div>
  <div class="flags"><i></i><i></i></div>
</header>

<nav class="nav"><span>Company</span><span>Trading Platforms</span><span>Account Types</span><span>Trading Products</span><span>Education</span><span>Promotions</span><span>Partnerships</span></nav>

<section class="hero" role="img" aria-label="Upward view of glass office towers against a blue sky">
  <h1>Low Cost Trading with a Leading Online Stock Broker</h1>
  <div class="strap">Trade global markets with tight spreads</div><br>
  <span class="btn btn-outline">Open Live Account</span>
</section>

<section class="platform">
  <div class="copy">
    <div class="label">Platforms</div>
    <h2>A Powerful Trading Platform to fit your Trading Style</h2>
    <p>Trade currencies, indices and commodities from desktop, web or mobile with fast execution, live charts and advanced tools built for every level of trader.</p>
    <span class="btn btn-yellow">Learn More</span>
  </div>
  <div class="devices" role="img" aria-label="Desktop, laptop, tablet and phone showing trading charts"></div>
</section>

<section class="features">
  <p class="intro">Our fee offers the features that you need in order to trade.<br>Pick yours, and we make it easy to compare.</p>
  <div class="feature-row">
    <span class="arrow">‹</span>
    <div class="feature"><svg width="40" height="40" viewBox="0 0 40 40" fill="none" stroke="#3f5667" stroke-width="2"><rect x="8" y="6" width="24" height="28"/><path d="M13 14h14M13 20h14M13 26h9"/></svg>Three Simplified Account Types</div>
    <div class="feature"><svg width="40" height="40" viewBox="0 0 40 40" fill="none" stroke="#3f5667" stroke-width="2"><rect x="6" y="10" width="20" height="24"/><rect x="14" y="6" width="20" height="24" fill="#fff"/></svg>Open a Trade Without Commission</div>
    <div class="feature"><svg width="40" height="40" viewBox="0 0 40 40" fill="none" stroke="#3f5667" stroke-width="2"><rect x="5" y="8" width="30" height="20"/><path d="M15 34h10M20 28v6"/></svg>Access on Any Device, Any Time</div>
    <div class="feature"><svg width="40" height="40" viewBox="0 0 40 40" fill="none" stroke="#3f5667" stroke-width="2"><path d="M6 34h28M6 6v28"/><path d="M10 28l7-9 6 5 9-13" stroke="#f2be2c"/></svg>Trade 60+ Forex Pairs and CFDs</div>
    <span class="arrow">›</span>
  </div>
  <span class="btn btn-outline">Compare Accounts</span>
</section>

<section class="showcase">
  <div class="photo" role="img" aria-label="Hands over a desk with printed financial charts and a tablet"></div>
  <div class="card card-yellow">
    <h3>Partnerships</h3>
    <p>Grow your business with a trusted broker, competitive rebates, dedicated managers and fast monthly payouts.</p>
    <span class="btn btn-outline">Learn More</span>
  </div>
  <div class="card card-slate">
    <h3>Education</h3>
    <p>Sharpen your skills with free webinars, market guides and daily analysis from our team of experienced analysts, available for all clients.</p>
    <span class="btn btn-outline">Learn More</span>
  </div>
</section>

<section class="why">
  <div class="label">Our Edge</div>
  <h2>Why Choose Our Pro Trader?</h2>
  <div class="why-row">
    <div class="why-item"><svg width="50" height="50" viewBox="0 0 50 50" fill="none" stroke="#f2be2c" stroke-width="2"><path d="M8 42h34"/><rect x="12" y="26" width="6" height="16"/><rect x="22" y="18" width="6" height="24"/><rect x="32" y="10" width="6" height="32"/></svg><b>Low Spreads</b>Tight pricing on major pairs</div>
    <div class="why-item"><svg width="50" height="50" viewBox="0 0 50 50" fill="none" stroke="#f2be2c" stroke-width="2"><circle cx="25" cy="25" r="16"/><path d="M25 15v10l7 5"/></svg><b>Fast Execution</b>Orders filled in milliseconds</div>
    <div class="why-item"><svg width="50" height="50" viewBox="0 0 50 50" fill="none" stroke="#f2be2c" stroke-width="2"><rect x="8" y="10" width="34" height="24"/><path d="M18 42h14M25 34v8"/></svg><b>Pro Tools</b>Advanced charts and indicators</div>
    <div class="why-item"><svg width="50" height="50" viewBox="0 0 50 50" fill="none" stroke="#f2be2c" stroke-width="2"><path d="M26 8h14v14L22 40 8 26z"/><circle cx="34" cy="14" r="2"/></svg><b>Pricing</b>Clear fees with no surprises</div>
  </div>
  <span class="btn btn-outline">Open Account Today</span>
</section>

<section class="help">
  <div class="help-deco" role="img" aria-label="Decorative market chart band in yellow leading into the help area"></div>
  <div class="inner">
    <div class="contact">
      <h4>Need Help?</h4>
      <p>Call Us Free: +00 555 0142</p>
      <p>Mail Us: help@vorquilatrade.example</p>
      <span class="btn">Contact Us Now</span>
    </div>
    <div>
      <h4>Request Call Back</h4>
      <div class="form">
        <div class="field">Full Name</div>
        <div class="field">Email Address</div>
        <div class="field">Phone Number</div>
        <div class="field">Preferred Time</div>
        <span class="btn">Submit</span>
      </div>
    </div>
  </div>
</section>

<footer class="footer">
  <div class="col"><h5>Vorquila Trade</h5>About Us<br>Regulation<br>Careers<br>Press Room<h5 style="margin-top:14px">Legal</h5>Privacy Policy<br>Terms of Use</div>
  <div class="col"><h5>Trading Platforms</h5>Desktop Platform<br>Web Trader<br>Mobile Apps<br>Platform Guides<h5 style="margin-top:14px">Account Types</h5>Standard<br>Premium<br>Islamic</div>
  <div class="col"><h5>Trading Products</h5>Forex<br>Indices<br>Commodities<br>Metals<br>Energies<br>Trading Hours</div>
  <div class="col"><h5>Education</h5>Webinars<br>Market News<br>Economic Calendar<br>Glossary<br>Video Lessons</div>
  <div class="col"><h5>Get Our App</h5><div class="store"></div><div class="store"></div><h5 style="margin-top:10px">Follow Us</h5><div class="social"><i></i><i></i><i></i><i></i></div></div>
</footer>
<div class="copyright">© 2024 Vorquila Trade. All rights reserved. Trading involves risk.</div>

</body>
</html>
```